Cardiology practice business card

We need a business card for our cardiology practice "Wattle Cardiology". We have a new logo, attached below. We like the colours in the logo - red and charcoal. The front of the business card will need to have the doctors name, address, phone number and email. The back will need to have space to write 2 appointment dates and times.

```html
<!DOCTYPE html>
<html lang="en">
<head>
<meta charset="utf-8">
<title>Wattle Cardiology – Business Card</title>
<link rel="stylesheet" href="https://fonts.googleapis.com/css2?family=Montserrat:wght@400;500;700&display=swap">
<style>
  :root {
    --red: #e0312b;
    --charcoal: #2b2e31;
    --grey: #55585c;
    --ink: #3a3a3a;
    --paper: #ffffff;
    --stage: #2f2f2f;
  }
  * { margin: 0; padding: 0; box-sizing: border-box; }
  html, body { width: 1200px; height: 875px; overflow: hidden; }
  body {
    background: var(--stage);
    font-family: "Montserrat", Arial, sans-serif;
    display: flex;
    align-items: center;
    justify-content: center;
    gap: 40px;
  }
  .card {
    position: relative;
    width: 540px;
    height: 310px;
    background: var(--paper);
    border-radius: 20px;
    overflow: hidden;
  }
  .brand {
    position: absolute;
    display: flex;
    align-items: center;
    gap: 10px;
    color: var(--red);
    font-weight: 700;
    letter-spacing: 1px;
    text-transform: uppercase;
    white-space: nowrap;
  }
  .brand-dot {
    width: 14px; height: 14px;
    border-radius: 50%;
    background: var(--red);
    flex: none;
  }

  /* Back: appointment card */
  .appointment .brand { top: 40px; right: 40px; font-size: 22px; }
  .appointment .title {
    position: absolute;
    left: 40px; top: 150px;
    color: var(--red);
    font-weight: 700;
    font-size: 22px;
  }
  .appointment .field {
    position: absolute;
    left: 40px; right: 40px;
    display: flex;
    align-items: flex-end;
    gap: 8px;
    font-size: 13px;
    font-weight: 500;
    color: var(--ink);
  }
  .appointment .field .line { flex: 1; border-bottom: 1px solid var(--grey); height: 1px; }
  .appointment .rule {
    position: absolute; left: 230px; right: 40px;
    border-bottom: 1px solid var(--grey);
  }
  .appointment .rule-1 { top: 95px; }
  .appointment .rule-2 { top: 130px; }
  .appointment .field-time { top: 200px; }
  .appointment .field-date { top: 245px; }

  /* Front: contact card */
  .contact .wave { position: absolute; inset: 0; }
  .contact .brand { top: 50px; right: 36px; font-size: 24px; }
  .contact .person { position: absolute; left: 32px; top: 95px; }
  .contact .name { color: var(--red); font-weight: 700; font-size: 21px; }
  .contact .role { color: var(--ink); font-size: 12px; margin-top: 2px; }
  .contact .address {
    position: absolute; left: 32px; top: 155px;
    font-size: 12px; line-height: 1.4; color: var(--ink);
  }
  .contact .details {
    position: absolute; left: 32px; top: 198px;
    list-style: none; font-size: 12px; color: var(--ink);
  }
  .contact .details li { display: flex; align-items: center; gap: 8px; height: 20px; }
  .contact .details svg { width: 11px; height: 11px; fill: var(--red); flex: none; }
</style>
</head>
<body>

  <section class="card appointment">
    <div class="brand"><span class="brand-dot"></span>Wattle Cardiology</div>
    <div class="rule rule-1"></div>
    <div class="rule rule-2"></div>
    <h2 class="title">Next Apointment</h2>
    <div class="field field-time"><span>Time:</span><span class="line"></span></div>
    <div class="field field-date"><span>Date:</span><span class="line"></span></div>
  </section>

  <section class="card contact">
    <svg class="wave" viewBox="0 0 540 310" preserveAspectRatio="none" aria-hidden="true">
      <path d="M540 55 C522 160 450 195 365 222 C265 256 135 282 0 306 L0 310 L540 310 Z" fill="var(--red)"/>
      <path d="M540 75 C525 172 455 208 372 234 C272 266 140 292 0 312 L540 312 Z" fill="var(--charcoal)"/>
    </svg>
    <div class="brand"><span class="brand-dot"></span>Wattle Cardiology</div>
    <div class="person">
      <h1 class="name">Daniel Hart</h1>
      <p class="role">Managing Director</p>
    </div>
    <p class="address">415 Lakeview Ave, #112<br>Riverton, OH 430571</p>
    <ul class="details">
      <li>
        <svg viewBox="0 0 24 24"><path d="M6.6 10.8a15 15 0 0 0 6.6 6.6l2.2-2.2c.3-.3.7-.4 1-.2 1.1.4 2.3.6 3.6.6.6 0 1 .4 1 1V20c0 .6-.4 1-1 1A17 17 0 0 1 3 4c0-.6.4-1 1-1h3.5c.6 0 1 .4 1 1 0 1.3.2 2.5.6 3.6.1.3 0 .7-.2 1z"/></svg>
        704-555-0148
      </li>
      <li>
        <svg viewBox="0 0 24 24"><path d="M2 5h20v14H2z M2 5l10 8 10-8"/></svg>
        info@wattlecardiology.com
      </li>
      <li>
        <svg viewBox="0 0 24 24"><circle cx="12" cy="12" r="10"/></svg>
        www.wattlecardiology.com
      </li>
    </ul>
  </section>

</body>
</html>
```